Art Nouveau Style Round Wine Label

I'd like to design a wine label:
- round
- Using art nouveau type feel similar to attached graphic
- Label should have the text: Morrowfen Vineyard, Pinot Noir, 2023

Target Market(s)

Private buyers - a unique small batch of wine

Industry/Entity Type

Wine

Colors
0054AA
0677BA
7BADD7
CADEEF
E8F1F8
0094D4
00A9DD
6FCCEA
C7EBF8
E9F6FB
00AB8E
00BBA5
67D7C9
C6EFE9
E9F9F6

Requirements
Must have
• Art Nouveau feel similar to the posted picture
Nice to have
• Keys and or Grape bunches incorporated instead of women's faces that are on the example graphic I posted

```html
<!DOCTYPE html>
<html lang="en">
<head>
<meta charset="utf-8">
<title>Morrowfen Vineyard – Pinot Noir 2023 Label</title>
<link rel="stylesheet" href="https://fonts.googleapis.com/css2?family=Oswald:wght@700&family=Special+Elite&family=Josefin+Sans:wght@700&display=swap">
<style>
  :root {
    --backdrop: #e4e4e4;
    --label-black: #0b0b0b;
    --gold-light: #f2c23a;
    --gold-mid: #d99a1c;
    --gold-deep: #b8720f;
  }
  html, body {
    margin: 0;
    padding: 0;
    width: 1200px;
    height: 1188px;
    overflow: hidden;
    background: var(--backdrop);
  }
  .label {
    display: block;
    width: 1200px;
    height: 1188px;
  }
  .label-disc { fill: var(--label-black); }
  .gold-line { fill: none; stroke: url(#goldFoil); stroke-width: 3; }
  .gold-fine { fill: none; stroke: url(#goldFoil); stroke-width: 2; }
  .side-stud { fill: var(--gold-mid); }
  .vineyard-name {
    font-family: "Oswald", "Arial Narrow", sans-serif;
    font-weight: 700;
    font-size: 128px;
    fill: url(#goldFoil);
  }
  .varietal {
    font-family: "Special Elite", "Courier New", monospace;
    font-size: 112px;
    fill: url(#goldFoil);
  }
  .vintage {
    font-family: "Josefin Sans", "Helvetica", sans-serif;
    font-weight: 700;
    font-size: 46px;
    letter-spacing: 20px;
    fill: var(--gold-deep);
  }
</style>
</head>
<body>
<svg class="label" viewBox="0 0 1200 1188" xmlns="http://www.w3.org/2000/svg">
  <defs>
    <linearGradient id="goldFoil" x1="0" y1="0" x2="1" y2="1">
      <stop offset="0" stop-color="var(--gold-light)"/>
      <stop offset="0.55" stop-color="var(--gold-mid)"/>
      <stop offset="1" stop-color="var(--gold-deep)"/>
    </linearGradient>
    <radialGradient id="medallionGlow" cx="0.5" cy="0.5" r="0.5">
      <stop offset="0" stop-color="var(--gold-mid)" stop-opacity="0.55"/>
      <stop offset="1" stop-color="var(--gold-deep)" stop-opacity="0.15"/>
    </radialGradient>
    <path id="nameArc" d="M323,695 A295,295 0 1,1 877,695"/>
    <path id="varietalArc" d="M321,789 A340,340 0 0,0 879,789"/>
  </defs>

  <!-- label body -->
  <circle class="label-disc" cx="600" cy="594" r="562"/>

  <!-- outer ornamental border -->
  <circle class="gold-line" cx="600" cy="594" r="553"/>
  <circle role="img" aria-label="Gold interlaced fret border band" cx="600" cy="594" r="527" fill="none" stroke="url(#goldFoil)" stroke-width="44" stroke-opacity="0.55"/>
  <circle class="gold-line" cx="600" cy="594" r="502"/>

  <!-- brick ring -->
  <circle class="gold-fine" cx="600" cy="594" r="470"/>
  <circle cx="600" cy="594" r="486" fill="none" stroke="url(#goldFoil)" stroke-width="32" stroke-dasharray="2 61.5"/>
  <circle class="gold-fine" cx="600" cy="594" r="455"/>

  <!-- side studs -->
  <circle class="side-stud" role="img" aria-label="Gold ornamental side stud" cx="80" cy="594" r="42"/>
  <circle class="side-stud" role="img" aria-label="Gold ornamental side stud" cx="1120" cy="594" r="42"/>

  <!-- accent arcs beside varietal -->
  <path class="gold-fine" d="M228,767 A410,410 0 0,0 395,949"/>
  <path class="gold-fine" d="M805,949 A410,410 0 0,0 972,767"/>
  <path class="gold-fine" d="M250,760 A385,385 0 0,0 360,905"/>
  <path class="gold-fine" d="M840,905 A385,385 0 0,0 950,760"/>

  <!-- vineyard name -->
  <text class="vineyard-name">
    <textPath href="#nameArc" startOffset="50%" text-anchor="middle" textLength="1080" lengthAdjust="spacingAndGlyphs">MORROWFEN VINEYARD</textPath>
  </text>

  <!-- central medallion -->
  <circle class="gold-fine" cx="600" cy="594" r="234"/>
  <circle cx="600" cy="594" r="208" fill="none" stroke="url(#goldFoil)" stroke-width="40"/>
  <circle cx="600" cy="594" r="208" fill="none" stroke="var(--label-black)" stroke-width="16" stroke-dasharray="16 26.2"/>
  <circle class="gold-fine" cx="600" cy="594" r="176"/>
  <circle role="img" aria-label="Gold star-shaped lace ornament" cx="600" cy="594" r="130" fill="url(#medallionGlow)"/>

  <!-- varietal -->
  <text class="varietal">
    <textPath href="#varietalArc" startOffset="50%" text-anchor="middle" textLength="600" lengthAdjust="spacingAndGlyphs">PINOT NOIR</textPath>
  </text>

  <!-- vintage ribbon -->
  <g class="vintage-ribbon">
    <path d="M410,1028 Q600,1012 790,1028 L780,1066 L792,1104 Q600,1090 408,1104 L420,1066 Z" fill="var(--label-black)" stroke="url(#goldFoil)" stroke-width="3"/>
    <path class="gold-fine" d="M432,1040 Q600,1026 768,1040"/>
    <text class="vintage" x="610" y="1082" text-anchor="middle">2023</text>
  </g>
</svg>
</body>
</html>
```